Business Card/Letterhead Design

We have our Logo, we simply need it cleaned up. Along with a letterhead design. It's pretty simple really.
Instead of the "Corporation" beside the logo. We need it to say "Limited" just under the logo between the "F" and the "Y"
The letter head has to have our address. 4375 Calverton Road Mississauga, ON L4W 2K7 Canada
Updates
Reason: I have been called out of town until Monday of next week.
Industry/Entity Type
Business
Contact Information for Business Card
4375 Calverton Road Mississauga, ON L4W 2K7 Canada
Look and feel
Each slider illustrates characteristics of the customer's brand and the style your logo design should communicate.

```html
<!DOCTYPE html>
<html lang="en">
<head>
<meta charset="utf-8">
<title>Velmora Limited – Business Card</title>
<link href="https://fonts.googleapis.com/css2?family=Source+Sans+3:wght@400;600;700&display=swap" rel="stylesheet">
<style>
  :root {
    --backdrop: #e4e4e6;
    --card: #ffffff;
    --panel: #dcdce0;
    --brand-blue: #4a4aa4;
    --brand-tan: #c9a273;
    --ink: #1b1b1f;
    --name-blue: #3b3f9c;
  }
  * { box-sizing: border-box; margin: 0; padding: 0; }
  html, body { width: 1200px; height: 900px; overflow: hidden; }
  body {
    background: var(--backdrop);
    font-family: "Source Sans 3", Arial, sans-serif;
    color: var(--ink);
    position: relative;
  }
  .card {
    position: absolute;
    left: 250px;
    width: 700px;
    height: 400px;
    background: var(--card);
    overflow: hidden;
    box-shadow: 0 4px 14px rgba(0,0,0,0.18);
  }
  .card--back { top: 35px; }
  .card--front { top: 465px; }

  .stripe-tan, .stripe-blue { position: absolute; left: 0; right: 0; }
  .stripe-tan { background: var(--brand-tan); height: 7px; }
  .stripe-blue { background: var(--brand-blue); }

  .card--back .stripe-tan { top: 300px; }
  .card--back .stripe-blue { top: 307px; height: 60px; }

  .wordmark {
    display: flex;
    align-items: center;
    gap: 14px;
    color: var(--brand-blue);
    font-weight: 600;
    white-space: nowrap;
  }
  .wordmark__dot {
    width: 44px; height: 44px;
    border-radius: 50%;
    background: var(--brand-tan);
    flex: none;
  }
  .card--back .wordmark {
    position: absolute;
    top: 122px; left: 0; right: 0;
    justify-content: center;
    font-size: 48px;
  }

  .card--front .panel {
    position: absolute;
    top: 180px; left: 0; right: 0; height: 190px;
    background: var(--panel);
  }
  .card--front .stripe-tan { top: 300px; }
  .card--front .stripe-blue { top: 307px; height: 60px; }
  .card--front .wordmark {
    position: absolute;
    top: 92px; left: 36px;
    font-size: 36px;
    gap: 12px;
  }
  .card--front .wordmark__dot { width: 34px; height: 34px; }

  .person {
    position: absolute;
    top: 80px; right: 40px;
    text-align: right;
  }
  .person__name {
    color: var(--name-blue);
    font-weight: 700;
    font-size: 23px;
    letter-spacing: 0.5px;
  }
  .person__title { font-size: 18px; font-weight: 600; margin-top: 2px; }

  .contact {
    position: absolute;
    font-size: 16px;
    font-weight: 600;
    line-height: 25px;
  }
  .contact--address { left: 28px; top: 196px; }
  .contact--phones { left: 280px; top: 221px; }
  .contact--web { left: 470px; top: 221px; }
  .contact__row { display: flex; align-items: center; gap: 7px; }
  .contact__row--indent { padding-left: 19px; }
  .icon { width: 12px; height: 12px; flex: none; fill: var(--brand-blue); }
</style>
</head>
<body>

  <section class="card card--back" aria-label="Business card back">
    <div class="wordmark"><span class="wordmark__dot"></span>Velmora Limited</div>
    <div class="stripe-tan"></div>
    <div class="stripe-blue"></div>
  </section>

  <section class="card card--front" aria-label="Business card front">
    <div class="panel"></div>
    <div class="stripe-tan"></div>
    <div class="stripe-blue"></div>

    <div class="wordmark"><span class="wordmark__dot"></span>Velmora Limited</div>

    <div class="person">
      <div class="person__name">ALDREN VOSS</div>
      <div class="person__title">Managing Director</div>
    </div>

    <div class="contact contact--address">
      <div class="contact__row">
        <svg class="icon" viewBox="0 0 12 12"><path d="M6 0a4 4 0 0 0-4 4c0 3 4 8 4 8s4-5 4-8a4 4 0 0 0-4-4zm0 5.5a1.5 1.5 0 1 1 0-3 1.5 1.5 0 0 1 0 3z"/></svg>
        1234, Address Goes Here,
      </div>
      <div class="contact__row contact__row--indent">Country Name, 123456</div>
    </div>

    <div class="contact contact--phones">
      <div class="contact__row">
        <svg class="icon" viewBox="0 0 12 12"><path d="M1 4c0-2 2-3 5-3s5 1 5 3v1H8V4H4v1H1zM3 6h6l1 5H2z"/></svg>
        123.456.7890
      </div>
      <div class="contact__row">
        <svg class="icon" viewBox="0 0 12 12"><path d="M3 0h6a1 1 0 0 1 1 1v10a1 1 0 0 1-1 1H3a1 1 0 0 1-1-1V1a1 1 0 0 1 1-1zm0 2v7h6V2z"/></svg>
        123.456.7890
      </div>
    </div>

    <div class="contact contact--web">
      <div class="contact__row">
        <svg class="icon" viewBox="0 0 12 12"><path d="M0 2h12v1L6 7 0 3zm0 2.4 6 4 6-4V10H0z"/></svg>
        info@youremail.com
      </div>
      <div class="contact__row">
        <svg class="icon" viewBox="0 0 12 12"><path d="M5 7 7 5M4.5 5.5 3 7a2 2 0 0 0 2.8 2.8L7.3 8.3M7.5 6.5 9 5A2 2 0 0 0 6.2 2.2L4.7 3.7" fill="none" stroke="#4a4aa4" stroke-width="1.5" stroke-linecap="round"/></svg>
        www.website.com
      </div>
    </div>
  </section>

</body>
</html>
```